Bright Loom Allies, LLC
Collaborative Contract Solutions
Modern
Owen Darby
Managing Director
12 Juniper Vale Road
Suite 240
Danvers, MA 01847
owen@brightloomallies.com
www.brightloomallies.com
Docs said to upload this logo format.

```html
<!DOCTYPE html>
<html lang="en">
<head>
<meta charset="utf-8">
<title>Bright Loom Allies, LLC — Stationery</title>
<link rel="stylesheet" href="https://fonts.googleapis.com/css2?family=Open+Sans:wght@400;600;700&display=swap">
<style>
:root{
  --bg:#3a3b3d;
  --paper:#ffffff;
  --blue:#1b57b0;
  --blue-deep:#0d3275;
  --blue-light:#4f8fe0;
  --ink:#2c3a55;
  --muted:#7b8494;
  --grey-flap:#b9bcc1;
}
*{margin:0;padding:0;box-sizing:border-box}
html,body{width:1200px;height:302px;overflow:hidden;background:var(--bg);font-family:"Open Sans",Arial,sans-serif;color:var(--ink)}
.stage{position:relative;width:1200px;height:302px}
.sheet{position:absolute;background:var(--paper);overflow:hidden;box-shadow:0 2px 6px rgba(0,0,0,.35)}
.sheet svg.swoosh{position:absolute;left:0;width:100%;height:100%;top:0}
.brand{position:absolute;display:flex;align-items:center;gap:4px;font-weight:700;color:var(--blue);white-space:nowrap}
.brand .dot{border-radius:50%;background:var(--blue);flex:none}
.small{position:absolute;font-size:4px;line-height:5.5px;color:var(--muted);white-space:nowrap}
.small strong{color:var(--ink);font-weight:600}
.card-blue{background:var(--blue)}
.card-blue .brand{color:#fff}
.card-blue .brand .dot{background:#fff}
.faint{position:absolute;font-weight:700;color:rgba(27,87,176,.08);white-space:nowrap}
.envelope-flap{position:absolute;left:0;top:0;width:100%;height:100%}
</style>
</head>
<body>
<main class="stage">

  <!-- Business cards -->
  <section class="sheet business-card front" style="left:29px;top:108px;width:118px;height:70px">
    <svg class="swoosh" viewBox="0 0 118 70" preserveAspectRatio="none"><path d="M0 60 Q60 52 118 66 L118 70 L0 70Z" fill="var(--blue)"/></svg>
    <div class="brand" style="left:12px;top:16px;font-size:6px"><span class="dot" style="width:10px;height:10px"></span>Bright Loom Allies</div>
    <div class="small" style="left:12px;top:31px"><strong>Owen Darby</strong><br>Managing Director</div>
  </section>
  <section class="sheet business-card back" style="left:154px;top:108px;width:118px;height:70px">
    <svg class="swoosh" viewBox="0 0 118 70" preserveAspectRatio="none"><path d="M0 0 L118 0 L118 8 Q60 2 0 12Z" fill="var(--blue)"/></svg>
    <div class="small" style="left:10px;top:18px"><strong>Owen Darby</strong><br>Managing Director<br>12 Juniper Vale Road, Suite 240<br>Danvers, MA 01847<br>owen@brightloomallies.com<br>www.brightloomallies.com</div>
  </section>
  <section class="sheet business-card plain" style="left:29px;top:192px;width:118px;height:70px">
    <div class="brand" style="left:14px;top:30px;font-size:7px"><span class="dot" style="width:11px;height:11px"></span>Bright Loom Allies</div>
  </section>
  <section class="sheet business-card card-blue" style="left:154px;top:192px;width:118px;height:70px">
    <div class="brand" style="left:14px;top:30px;font-size:7px"><span class="dot" style="width:11px;height:11px"></span>Bright Loom Allies</div>
  </section>

  <!-- Letterhead -->
  <section class="sheet letterhead" style="left:293px;top:19px;width:182px;height:264px">
    <svg class="swoosh" viewBox="0 0 182 264" preserveAspectRatio="none">
      <path d="M0 0 L12 0 Q10 130 22 264 L0 264Z" fill="var(--blue)"/>
      <path d="M0 250 Q90 236 182 252 L182 264 L0 264Z" fill="var(--blue-deep)"/>
    </svg>
    <div class="brand" style="left:36px;top:20px;font-size:6px"><span class="dot" style="width:10px;height:10px"></span>Bright Loom Allies</div>
    <div class="small" style="left:118px;top:16px">12 Juniper Vale Road<br>Suite 240<br>Danvers, MA 01847<br>www.brightloomallies.com</div>
    <div class="faint" style="left:52px;top:110px;font-size:16px">BLA</div>
  </section>

  <!-- Continuation sheet -->
  <section class="sheet letterhead continuation" style="left:499px;top:19px;width:183px;height:264px">
    <div class="faint" style="left:56px;top:110px;font-size:16px">BLA</div>
  </section>

  <!-- Compliment slip -->
  <section class="sheet compliment-slip" style="left:710px;top:84px;width:173px;height:89px">
    <svg class="swoosh" viewBox="0 0 173 89" preserveAspectRatio="none">
      <path d="M0 0 L10 0 Q8 45 16 89 L0 89Z" fill="var(--blue)"/>
      <path d="M0 80 Q90 70 173 82 L173 89 L0 89Z" fill="var(--blue-deep)"/>
    </svg>
    <div class="brand" style="left:24px;top:12px;font-size:5px"><span class="dot" style="width:8px;height:8px"></span>Bright Loom Allies</div>
    <div class="small" style="left:24px;top:26px">12 Juniper Vale Road, Suite 240, Danvers, MA 01847</div>
  </section>

  <!-- Small envelope -->
  <section class="sheet small-envelope" style="left:710px;top:187px;width:173px;height:96px">
    <svg class="swoosh" viewBox="0 0 173 96" preserveAspectRatio="none">
      <path d="M0 86 Q90 76 173 88 L173 96 L0 96Z" fill="var(--blue)"/>
    </svg>
    <div class="brand" style="left:12px;top:12px;font-size:5px"><span class="dot" style="width:8px;height:8px"></span>Bright Loom Allies</div>
  </section>

  <!-- Envelopes -->
  <section class="sheet envelope back" style="left:893px;top:24px;width:283px;height:70px">
    <svg class="envelope-flap" viewBox="0 0 283 70" preserveAspectRatio="none">
      <path d="M0 0 L283 0 L283 22 L141 48 L0 22Z" fill="var(--grey-flap)"/>
      <path d="M0 62 Q140 52 283 64 L283 70 L0 70Z" fill="var(--blue)"/>
    </svg>
  </section>
  <section class="sheet envelope front" style="left:893px;top:108px;width:283px;height:80px">
    <svg class="swoosh" viewBox="0 0 283 80" preserveAspectRatio="none">
      <path d="M0 0 L14 0 Q10 40 20 80 L0 80Z" fill="var(--blue)"/>
      <path d="M0 72 Q140 62 283 74 L283 80 L0 80Z" fill="var(--blue-deep)"/>
    </svg>
    <div class="brand" style="left:28px;top:10px;font-size:5px"><span class="dot" style="width:8px;height:8px"></span>Bright Loom Allies</div>
    <div class="small" style="left:28px;top:24px">12 Juniper Vale Road<br>Suite 240, Danvers, MA 01847</div>
  </section>
  <section class="sheet envelope open" style="left:893px;top:200px;width:283px;height:82px">
    <svg class="envelope-flap" viewBox="0 0 283 82" preserveAspectRatio="none">
      <path d="M0 0 L141 40 L283 0Z" fill="var(--blue-light)"/>
      <path d="M0 0 L141 36 L283 0 L283 6 L141 44 L0 6Z" fill="var(--blue)"/>
      <path d="M0 74 Q140 64 283 76 L283 82 L0 82Z" fill="var(--blue)"/>
    </svg>
  </section>

</main>
</body>
</html>
```